Plumbing Business needs a more appealing business card design and logo

card must include phone number and logo, open to new logo ideas, full creative freedom

Industry/Entity Type

Plumbing

Contact Information for Business Card

Derek Halloway
0417385521

Logo Text

call outs from $80

Font styles to use
Other font styles liked:
• unsure

Colors
ec1f27
0255a3
f78f20

```html
<!DOCTYPE html>
<html lang="en">
<head>
<meta charset="utf-8">
<title>Bellamy's Plumbing – Business Card</title>
<link rel="stylesheet" href="https://fonts.googleapis.com/css2?family=Lato:wght@300;400;700&display=swap">
<style>
  :root {
    --page-bg: #d9d9d9;
    --brand-blue: #0a4f9c;
    --brand-blue-light: #0f5cb0;
    --brand-blue-dark: #073f86;
    --band-dark: #1f1f1f;
    --ink: #1c1c1c;
    --white: #ffffff;
    --paper-top: #ffffff;
    --paper-bottom: #d6d6d6;
  }
  * { box-sizing: border-box; margin: 0; padding: 0; }
  html, body {
    width: 1200px; height: 1176px; overflow: hidden;
    background: var(--page-bg);
    font-family: "Lato", sans-serif;
  }
  .card {
    position: absolute; left: 200px; width: 782px;
    border-radius: 26px; overflow: hidden;
    box-shadow: 0 6px 14px rgba(0,0,0,0.25);
  }
  .card--front { top: 97px; height: 448px; background: var(--white); }
  .card--back {
    top: 596px; height: 446px;
    background: linear-gradient(160deg, var(--brand-blue-light), var(--brand-blue-dark));
  }
  .front-top {
    position: absolute; left: 0; top: 0; width: 100%; height: 255px;
    background: linear-gradient(180deg, var(--paper-top), var(--paper-bottom));
  }
  .wordmark {
    position: absolute; left: 0; width: 100%;
    display: flex; justify-content: center; align-items: center; gap: 16px;
    font-weight: 700;
  }
  .wordmark__dot { border-radius: 50%; flex: none; }
  .wordmark__text { display: flex; flex-direction: column; align-items: flex-end; line-height: 1; }
  .wordmark__name { font-size: 58px; letter-spacing: 1px; }
  .wordmark__trade { font-size: 22px; letter-spacing: 14px; margin-top: 10px; margin-right: -14px; }
  .wordmark--front { top: 105px; color: var(--brand-blue); }
  .wordmark--front .wordmark__dot { width: 40px; height: 40px; background: var(--brand-blue); }
  .wordmark--back { top: 170px; color: var(--white); }
  .wordmark--back .wordmark__dot { width: 44px; height: 44px; background: var(--white); }
  .contact-band {
    position: absolute; left: 0; top: 255px; width: 100%; height: 136px;
    background: var(--band-dark);
  }
  .holder {
    position: absolute; right: 412px; top: 38px; text-align: right;
  }
  .holder__name { color: var(--white); font-size: 29px; font-weight: 300; letter-spacing: 0.5px; white-space: nowrap; }
  .holder__name strong { font-weight: 700; }
  .holder__role { color: var(--brand-blue-light); font-size: 19px; margin-top: 6px; letter-spacing: 0.5px; }
  .divider {
    position: absolute; left: 390px; top: 25px; width: 2px; height: 91px;
    background: var(--brand-blue);
  }
  .contact-list { position: absolute; left: 408px; top: 24px; list-style: none; }
  .contact-list li {
    display: flex; align-items: center; gap: 10px;
    color: var(--white); font-size: 19px; height: 33px;
  }
  .contact-list svg { width: 17px; height: 17px; fill: var(--brand-blue-light); }
  .rule { position: absolute; left: 0; top: 391px; width: 100%; height: 4px; background: var(--white); }
  .tagline-band {
    position: absolute; left: 0; top: 395px; width: 100%; height: 53px;
    background: var(--brand-blue);
    color: var(--white); font-size: 19px;
    display: flex; justify-content: center; align-items: center; padding-bottom: 8px;
    word-spacing: 6px;
  }
</style>
</head>
<body>
  <section class="card card--front">
    <div class="front-top">
      <div class="wordmark wordmark--front">
        <span class="wordmark__dot"></span>
        <div class="wordmark__text">
          <span class="wordmark__name">BELLAMY'S</span>
          <span class="wordmark__trade">PLUMBING</span>
        </div>
      </div>
    </div>
    <div class="contact-band">
      <div class="holder">
        <p class="holder__name">DEREK <strong>HALLOWAY</strong></p>
        <p class="holder__role">OWNER</p>
      </div>
      <div class="divider"></div>
      <ul class="contact-list">
        <li><svg viewBox="0 0 24 24"><path d="M2 9c0-3 4-5 10-5s10 2 10 5v2h-5V8.5c-1.5-.6-3.2-.9-5-.9s-3.5.3-5 .9V11H2z M5 13h14l2 7H3z"/></svg>0417385521</li>
        <li><svg viewBox="0 0 24 24"><path d="M2 5h20v14H2z M3 6l9 7 9-7" stroke="#1f1f1f" stroke-width="1.5"/></svg>hello@bellamyplumbing.com</li>
        <li><svg viewBox="0 0 24 24"><path d="M12 2a7 7 0 0 0-7 7c0 5 7 13 7 13s7-8 7-13a7 7 0 0 0-7-7zm0 9.5A2.5 2.5 0 1 1 12 6.5a2.5 2.5 0 0 1 0 5z"/></svg>Address here</li>
      </ul>
    </div>
    <div class="rule"></div>
    <div class="tagline-band">Services &nbsp;I&nbsp; You &nbsp;I&nbsp; Provide</div>
  </section>

  <section class="card card--back">
    <div class="wordmark wordmark--back">
      <span class="wordmark__dot"></span>
      <div class="wordmark__text">
        <span class="wordmark__name">BELLAMY'S</span>
        <span class="wordmark__trade">PLUMBING</span>
      </div>
    </div>
  </section>
</body>
</html>
```